Brackenford Group Website

We have a newly established brand for a company with an existing portfolio of property. The company is corporate and professional and both owns and develops property. The website should reflect a professional and stable organisation. The website should showcase the existing properties (6), have a home page that describes the company and its activities and has a "about us" page. The website will be in Wordpress and we would like the code for all pages to be sent to us by the successful designer upon completion of the job.

sorry was called from the office on an urgent matter. To be fair on submitters, i need a couple more days to finalise reviews.

Contact Information for Business Card

Brackenford Logo on front
Black background with silver logo.

Coding

Number of Pages Required

5+ page

Colors

Designer to choose colors to be used in the design.

Requirements
Must have
• Text side of card should include
• Brackenford Property Group (as title in logo font)
• Employee Name (centered)
• Job Title (centered below name)
• Address 4 lines
• Email, mobile office phone, 3 lines
• website address (probably as footer)

```html
<!DOCTYPE html>
<html lang="en">
<head>
<meta charset="utf-8">
<title>Brackenford Group</title>
<link href="https://fonts.googleapis.com/css2?family=Rajdhani:wght@500;600;700&family=Poppins:wght@300;400;500&display=swap" rel="stylesheet">
<style>
:root{
  --orange:#ffa200;
  --orange-deep:#f39200;
  --ink:#2b2b2b;
  --text:#4a4a4a;
  --grey-band:#f1f1f1;
  --light-band:#f7f7f7;
  --black:#0b0b0b;
  --white:#ffffff;
  --navy:#1c2f63;
}
*{margin:0;padding:0;box-sizing:border-box}
html,body{width:1200px;height:4074px;overflow:hidden;background:var(--white)}
body{position:relative;font-family:"Poppins",sans-serif;color:var(--text)}
.abs{position:absolute}
.head{font-family:"Rajdhani",sans-serif;font-weight:600;color:var(--ink)}
.btn{position:absolute;display:flex;align-items:center;justify-content:center;font-family:"Rajdhani",sans-serif;font-weight:700;font-size:14px;color:#2a1c00;text-decoration:none;background:linear-gradient(90deg,var(--orange) 0%,var(--orange) 55%,#ffe9bf 100%)}
.body-copy{font-size:9.5px;line-height:17px;color:var(--text);font-weight:300}

/* hero */
.hero{left:0;top:0;width:1200px;height:600px;background:linear-gradient(180deg,#1c3a8c 0%,#2a3f70 35%,#3a3b4a 70%,#1a1b22 100%)}
.logo-box{left:95px;top:0;width:126px;height:90px;border:1px solid rgba(255,255,255,.7);display:flex;flex-direction:column;align-items:center;justify-content:center;color:var(--white);font-family:"Rajdhani",sans-serif}
.logo-box .sq{width:14px;height:14px;border:1.5px solid var(--white);margin-bottom:6px}
.logo-box .name{font-size:11px;letter-spacing:1.5px;font-weight:600}
.nav{top:34px}
.nav a{position:absolute;white-space:nowrap;font-family:"Rajdhani",sans-serif;font-weight:600;font-size:13px;color:var(--white);text-decoration:none}
.nav a.on{color:var(--orange)}
.hero-title{left:0;width:1200px;top:232px;text-align:center;font-family:"Rajdhani",sans-serif;font-weight:700;color:var(--white);font-size:72px;line-height:80px}
.hero-sub{left:0;width:1200px;top:303px;text-align:center;font-family:"Rajdhani",sans-serif;font-weight:700;color:var(--white);font-size:47px;line-height:52px}
.hero-rule{left:368px;top:360px;width:390px;height:1px;background:rgba(255,255,255,.7)}

/* about */
.about-frame{left:95px;top:686px;width:387px;height:364px;background:var(--orange);clip-path:polygon(0 0,46% 0,48% 3%,100% 3%,100% 100%,0 100%)}
.about-photo{left:108px;top:699px;width:490px;height:340px;background:linear-gradient(180deg,#c9d3da 0%,#d8c9b4 45%,#3c3a38 100%)}

/* expertise */
.expertise{left:0;top:1135px;width:1200px;height:411px;background:var(--grey-band)}
.exp-photo{left:615px;top:1219px;width:492px;height:364px;background:linear-gradient(180deg,#5c6f8c 0%,#e1946a 30%,#8a4a34 60%,#3a2a28 100%)}
.arrow-btn{width:41px;height:39px;display:flex;align-items:center;justify-content:center}

/* case studies */
.case{position:absolute;width:331px;height:270px}
.case .label{position:absolute;left:19px;right:19px;bottom:0;height:63px;background:var(--white);display:flex;align-items:center;justify-content:center;font-family:"Rajdhani",sans-serif;font-weight:600;font-size:29px;color:#444}

/* detail */
.detail{left:0;top:2455px;width:1200px;height:617px;background:var(--light-band)}
.detail-photo{left:708px;top:2511px;width:402px;height:498px;background:linear-gradient(180deg,#9aa3a6 0%,#5a6266 50%,#2c3234 100%)}
.sub-head{font-family:"Rajdhani",sans-serif;font-weight:700;font-size:17px;color:var(--ink)}

/* team */
.team{left:0;top:3160px;width:1200px;height:508px;background:linear-gradient(180deg,#2a2a2a,#161616)}
.member{position:absolute;top:3290px;width:247px;height:318px;background:var(--white)}
.member .photo{height:220px;background:linear-gradient(180deg,#e9e9e9 0%,#bfc3c7 60%,#3b3f47 100%)}
.member .name{height:36px;border-bottom:1px solid #ddd;display:flex;align-items:center;justify-content:center;font-family:"Rajdhani",sans-serif;font-weight:600;font-size:16px;color:var(--ink)}
.member p{padding:10px 18px 0;text-align:center;font-size:9.5px;line-height:17px;color:var(--text)}

/* footer */
.footer{left:0;top:3753px;width:1200px;height:321px;background:var(--black)}
.foot-orange{left:378px;top:3753px;width:177px;height:321px;background:var(--orange)}
.foot-bar{left:555px;top:4046px;width:645px;height:28px;background:#1d1d1d;color:#8d8d8d;font-size:9px;display:flex;align-items:center;padding-left:54px}
.foot-bar b{color:var(--orange);font-weight:500}
.foot-h{font-family:"Rajdhani",sans-serif;font-weight:700;font-size:15px;color:var(--white)}
.foot-list{font-size:9.5px;line-height:23.5px;color:#cfcfcf}
.foot-list.dark{color:var(--white)}
.foot-addr{font-size:9px;line-height:15px;color:#cfcfcf}
</style>
</head>
<body>

<!-- Hero -->
<section class="abs hero" role="img" aria-label="Photo of modern glass apartment buildings against a blue sky"></section>
<div class="abs logo-box"><span class="sq"></span><span class="name">BRACKENFORD</span></div>
<nav class="abs nav">
  <a class="on" style="left:760px">About</a>
  <a style="left:818px">Expertise</a>
  <a style="left:896px">Case Studies</a>
  <a style="left:992px">Team</a>
  <a style="left:1049px">Contact Us</a>
</nav>
<h1 class="abs hero-title">Owned Commercial Real</h1>
<div class="abs hero-sub">Estate Investment Company</div>
<div class="abs hero-rule"></div>
<a class="btn" style="left:522px;top:381px;width:114px;height:38px;background:var(--orange)">Read More</a>

<!-- About -->
<div class="abs about-frame"></div>
<div class="abs about-photo" role="img" aria-label="Photo of a city skyline with cranes and high-rise towers"></div>
<h2 class="abs head" style="left:636px;top:714px;font-size:38px">About Us</h2>
<p class="abs body-copy" style="left:636px;top:774px;width:462px">
Brackenford Group is a privately-owned commercial real estate investment company founded in Auckland in 2007. Working with a small group of long-standing private and institutional partners, the firm has successfully acquired and developed assets valued at over $1.0 billion.<br>
Brackenford Group has a long track record of success in the acquisition, consenting, development, renovation and repositioning of office, tourism accommodation, residential, social housing, retail and mixed use properties within the Auckland region.<br>
Drawing upon the decades of experience of its principals, partners and the skill sets of the Brackenford team, the company has been able to identify many successful real estate investment opportunities, produce exceptional investment performance and provide lasting positive impacts on the tenants and communities it serves.
</p>
<a class="btn" style="left:636px;top:971px;width:107px;height:38px">Read More</a>

<!-- Expertise -->
<section class="abs expertise"></section>
<h2 class="abs head" style="left:612px;top:1157px;font-size:38px">Expertise</h2>
<div class="abs exp-photo" role="img" aria-label="Aerial photo of a dense city at sunset"></div>
<h3 class="abs head" style="left:95px;top:1258px;font-size:32px">Acquisitions</h3>
<p class="abs body-copy" style="left:95px;top:1313px;width:470px">
Prior to any successful real estate acquisition we plan and implement proactive and thoughtful market and asset research. The Brackenford team prides itself on our ability to evaluate market opportunities before others see them. We use our longstanding relationships with the brokerage and broader real estate community together with our reputation for "delivering on our promises" to purchase and position unique investment opportunities.
</p>
<a class="btn" style="left:96px;top:1420px;width:116px;height:38px">Read More</a>
<div class="abs arrow-btn" style="left:552px;top:1619px;background:#8a8a8a">
  <svg width="14" height="14" viewBox="0 0 14 14"><path d="M9 2 L4 7 L9 12" fill="none" stroke="#fff" stroke-width="2"/></svg>
</div>
<div class="abs arrow-btn" style="left:606px;top:1619px;background:#000">
  <svg width="14" height="14" viewBox="0 0 14 14"><path d="M5 2 L10 7 L5 12" fill="none" stroke="#fff" stroke-width="2"/></svg>
</div>

<!-- Case Studies -->
<h2 class="abs head" style="left:0;width:1200px;text-align:center;top:1740px;font-size:40px">Case Studies</h2>
<div class="case" style="left:93px;top:1813px;background:linear-gradient(180deg,#8d9aa3,#3f4a4f)" role="img" aria-label="Aerial photo of city towers"><div class="label">Ashgrove</div></div>
<div class="case" style="left:435px;top:1813px;background:linear-gradient(180deg,#b44a3a,#3a2e2e 60%,#1e2424)" role="img" aria-label="Photo of city buildings under a red sky"><div class="label">The Wexley</div></div>
<div class="case" style="left:776px;top:1813px;background:linear-gradient(180deg,#c7d2db,#b89a74 60%,#5d4a3a)" role="img" aria-label="Photo of a skyline of tall towers"><div class="label">Harlow</div></div>
<div class="case" style="left:93px;top:2100px;background:linear-gradient(180deg,#c8b590,#7a5a3a 60%,#3a3028)" role="img" aria-label="Photo of a street lined with old brick buildings"><div class="label">Dunmore</div></div>
<div class="case" style="left:435px;top:2100px;background:linear-gradient(180deg,#eeeeee,#c5c5c5 60%,#8a8a8a)" role="img" aria-label="Photo of a stone monument with statues"><div class="label">The Wexley</div></div>
<div class="case" style="left:776px;top:2100px;background:linear-gradient(180deg,#f2f2f2,#d8d8d8 60%,#9a8a80)" role="img" aria-label="Photo of a team meeting in a bright office"><div class="label">Six Twelve</div></div>

<!-- Detail -->
<section class="abs detail"></section>
<h2 class="abs head" style="left:96px;top:2541px;font-size:38px;line-height:50px;font-weight:700">Ashgrove. 48 Halden Av,<br>Auckland CBD</h2>
<div class="abs sub-head" style="left:96px;top:2661px">The vision</div>
<p class="abs body-copy" style="left:96px;top:2686px;width:560px;font-weight:400;font-size:9.5px;line-height:18px">The building was a run-down backpacker lodge with a low earthquake rating. In this gentrifying part of Auckland we saw the opportunity for a small boutique apartment building</p>
<div class="abs sub-head" style="left:96px;top:2733px">The Project</div>
<p class="abs body-copy" style="left:96px;top:2760px;width:560px;font-weight:400;font-size:9.5px;line-height:18px">
We added an extra floor to the building, and while retaining the front and rear walls, completely removed all internal partitions and walls. We strengthened walls and parapets and rebuilt the foundations insitu. New lifts were installed and all walls were plastered and repainted. Internally we laid quality carpet and specialty flooring throughout, upgraded the grand public stair, exposed services and sandblasted the side walls back to bare brick.<br>
We then laid out a modern series of apartments over 5 floors with a central corridor. We exposed the ceilings and services, installed quality fittings and specialty tapware and created a New York loft style.<br><br>
We fully fitted out all apartments with quality furnished, fabrics and soft goods.
</p>
<a class="btn" style="left:96px;top:2926px;width:116px;height:38px">Read More</a>
<div class="abs detail-photo" role="img" aria-label="Photo of twin skyscrapers above a city"></div>
<div class="abs arrow-btn" style="left:598px;top:3064px;width:57px;height:35px;background:var(--orange)">
  <svg width="22" height="14" viewBox="0 0 22 14"><path d="M3 3 L11 11 L19 3" fill="none" stroke="#000" stroke-width="2.5"/></svg>
</div>

<!-- Team -->
<section class="abs team" role="img" aria-label="Darkened photo of a business team"></section>
<h2 class="abs head" style="left:0;width:1200px;text-align:center;top:3222px;font-size:42px;color:var(--white);font-weight:700">Team Members</h2>
<div class="member" style="left:93px"><div class="photo" role="img" aria-label="Portrait photo of a team member in a suit"></div><div class="name">Marcus Hollow</div><p>Lorem Ipsum is simply dummy text of the printing and typesetting industry</p></div>
<div class="member" style="left:349px"><div class="photo" role="img" aria-label="Portrait photo of a team member in a suit" style="background:linear-gradient(90deg,#e8e8e8 0%,#d9d9d9 50%,#b8744a 70%,#8a4a2a 100%)"></div><div class="name">Ethan Lowe-Carrick</div><p>Lorem Ipsum is simply dummy text of the printing and typesetting industry</p></div>
<div class="member" style="left:605px"><div class="photo" role="img" aria-label="Portrait photo of a team member in a suit"></div><div class="name">Marcus Hollow</div><p>Lorem Ipsum is simply dummy text of the printing and typesetting industry</p></div>
<div class="member" style="left:860px"><div class="photo" role="img" aria-label="Portrait photo of a team member in a suit"></div><div class="name">Marcus Hollow</div><p>Lorem Ipsum is simply dummy text of the printing and typesetting industry</p></div>

<!-- Footer -->
<footer class="abs footer"></footer>
<div class="abs foot-orange"></div>
<div class="abs" style="left:95px;top:3800px;width:156px;display:flex;flex-direction:column;align-items:center">
  <span style="width:30px;height:30px;border:2px solid #fff"></span>
  <span style="font-family:'Rajdhani',sans-serif;font-weight:600;font-size:20px;letter-spacing:2px;color:#fff;margin-top:10px">BRACKENFORD</span>
  <span style="font-family:'Rajdhani',sans-serif;font-weight:600;font-size:8px;letter-spacing:3px;color:#fff">PROPERTY GROUP</span>
</div>
<p class="abs" style="left:95px;top:3898px;width:280px;font-size:10.5px;line-height:16px;color:#e0e0e0">Brackenford Group is a privately-owned commercial real estate investment company founded in Auckland in 2007. Working with a small group of long-standing private and institutional partners.</p>
<div class="abs" style="left:95px;top:3987px;width:38px;height:38px;border-radius:50%;background:#fff"></div>
<div class="abs" style="left:146px;top:3987px;width:38px;height:38px;border-radius:50%;background:#fff"></div>
<div class="abs" style="left:196px;top:3987px;width:38px;height:38px;border-radius:50%;background:#fff"></div>

<div class="abs foot-h" style="left:410px;top:3819px">Sitemap</div>
<div class="abs foot-list dark" style="left:411px;top:3867px">About<br>Expertise<br>Case Studies<br>Team<br>Contact Us</div>

<div class="abs foot-h" style="left:609px;top:3819px">Case Studies</div>
<div class="abs foot-list" style="left:609px;top:3868px">Ashgrove<br>The Wexley<br>Harlow<br>Dunmore<br>Fernhill<br>Six Twelve</div>

<div class="abs foot-h" style="left:740px;top:3819px">Contact Us</div>
<div class="abs foot-addr" style="left:740px;top:3871px">Brackenford Group Ltd<br>Level 6, Kestrel House<br>20 Merrow Lane<br>Auckland CBD<br><br>PO Box 4021<br>Waverley St<br>Auckland 1010</div>

<div class="abs foot-h" style="left:891px;top:3819px">Contact Us</div>
<div class="abs foot-addr" style="left:895px;top:3858px;line-height:20px">
  <div style="display:flex;align-items:center;gap:8px"><svg width="9" height="9" viewBox="0 0 10 10"><path d="M2 1 L4 1 L5 3.5 L3.8 4.5 Q5 6.5 6 6.5 L7 5.3 L9.5 6.3 L9.5 8.5 Q9 9.5 7.5 9.3 Q1 8 0.7 2.5 Q0.8 1 2 1Z" fill="#fff"/></svg>+64 9 555 0142</div>
  <div style="display:flex;align-items:center;gap:8px"><svg width="10" height="8" viewBox="0 0 10 8"><rect x="0.5" y="0.5" width="9" height="7" fill="none" stroke="#fff"/><path d="M0.5 0.5 L5 4.5 L9.5 0.5" fill="none" stroke="#fff"/></svg>marcus@brackenfordgroup.co.nz</div>
</div>
<div class="abs foot-h" style="left:896px;top:3903px">News Letter</div>
<div class="abs" style="left:896px;top:3930px;width:209px;height:27px;border:1px solid var(--orange);color:#8a8a8a;font-size:9px;display:flex;align-items:center;padding-left:10px">Enter Your Email</div>
<a class="btn" style="left:898px;top:3970px;width:114px;height:36px;background:var(--orange);font-size:13px">Subscribe Now</a>

<div class="abs foot-bar">©2019&nbsp;<b>BRACKENFORD PROPERTY GROUP</b>&nbsp;All rights reserved</div>

</body>
</html>
```